Professional Engineering Web Design

Project Brief: Website Redesign for Mechanical Design Consultancy
Project Overview
I want to update and improve my current website to create a more professional, modern, and high-credibility online presence for my mechanical design consultancy.

Current site: https://valtrobuild.design/

The new website must communicate expertise, precision, and trust—matching the standard of top engineering and product design agencies.

Reference Websites (Style + Structure Inspiration)
These represent the quality, cleanliness, and professionalism I want to achieve:

https://plinthformworks.com/
https://www.zorvanta.com/
https://quellory-uk.com/
Brand Look
Professional, modern, engineering-focused aesthetic
Clean layouts and strong typography
High-quality imagery conveying precision, innovation, and mechanical expertise
Colour scheme and styling must follow my existing logo (attached in project)
Platform Requirements
The website must be built on WordPress
Should use a clean, flexible theme or modern page builder (Elementor, Gutenberg, Bricks, or similar)
Avoid overly complex custom coding so I can easily edit content later
Final deliverable must allow me to manage and update content without developer assistance
Functionality
Fast-loading, lightweight, and smooth user experience
Clean animations and transitions similar to the reference sites
Fully mobile responsive
Clear navigation and strong visual hierarchy
Contact forms optimised for lead generation
Optional: subtle scroll effects, case study sliders, icon animations, etc.
SEO Aspirations
Developer should recommend and implement a modern SEO strategy
Proper on-page SEO setup (titles, meta, schema, alt tags, heading structure)
Optimised site architecture for ranking and crawling
Aim: Generate leads through improved visibility and keyword targeting
Optional but useful: Google Analytics, Google Search Console setup
User Journeys
(Recommended structure)

The site should be crafted around clear, intuitive journeys for each type of visitor:

Potential new clients
Quickly understand what services I offer
View examples of past work / case studies
See credibility indicators (process, expertise, industries served)
Easily contact me or request a project discussion
Returning clients
Access updated portfolio items
Find contact details or book follow-up work easily
General visitors discovering through SEO
Be guided to valtro service areas
Understand my value proposition quickly
Be invited to learn more or make contact
The developer should design the structure to support these journeys smoothly.

Maintenance Expectations
Website will be maintained by me, so it should be easy to update using relatively basic WordPress skills
Use modular templates and simple backend structure
Avoid unnecessary plugins
Provide brief handover documentation if required
Hosting Preferences
Site is currently hosted via a family member
Open to discussing moving to a paid, reliable hosting provider if preferable for performance and maintainability
Developer may advise on the best hosting setup for WordPress
Content
Most content can be taken from the existing website
Developer is welcome to suggest improvements to structure, layout, and imagery
Must remain easy for me to edit or add new content later (e.g., new projects)
Deliverables
Fully built WordPress website
Clean, professional, modern design inspired by the reference sites
Mobile-responsive across all devices
SEO-ready structure and optimisations
Transfer of website and admin rights
Any design assets, templates, or documentation used

```html
<!DOCTYPE html>
<html lang="en">
<head>
<meta charset="utf-8">
<title>Valtro Mechanical Design</title>
<link href="https://fonts.googleapis.com/css2?family=Outfit:wght@400;500;600;700;800&family=DM+Sans:wght@400;500;700&display=swap" rel="stylesheet">
<style>
:root{
  --blue:#2f5cf0;
  --blue-dark:#1f3fc4;
  --ink:#1c1c22;
  --grey:#4a4a4f;
  --dark:#19191c;
  --pale:#eef1fd;
  --line:#d5dbef;
  --white:#ffffff;
  --muted:#5c6070;
}
*{box-sizing:border-box;margin:0;padding:0}
html,body{width:1200px;height:4736px;overflow:hidden}
body{position:relative;background:var(--white);font-family:"DM Sans",sans-serif;color:var(--ink)}
.abs{position:absolute}
h1,h2,h3,.heading{font-family:"Outfit",sans-serif}
.btn{position:absolute;display:flex;align-items:center;justify-content:space-between;height:38px;padding:0 6px 0 20px;border-radius:20px;background:var(--blue);color:#fff;font-family:"Outfit",sans-serif;font-size:12px;font-weight:600}
.btn .dot{width:28px;height:28px;border-radius:50%;background:#fff;display:flex;align-items:center;justify-content:center}
.btn .dot i{width:14px;height:14px;border-radius:50%;border:3px solid var(--blue)}
.btn.light{background:#fff;color:var(--blue)}
.btn.light .dot{background:var(--blue)}
.btn.light .dot i{border-color:#fff}
.logo{display:flex;align-items:center;gap:10px;color:#fff;font-family:"Outfit",sans-serif;font-size:28px;font-weight:600;letter-spacing:3px}
.logo .mark{width:38px;height:38px;border-radius:50%;background:var(--blue)}
.watermark{position:absolute;left:0;width:1200px;white-space:nowrap;overflow:hidden;font-family:"Outfit",sans-serif;font-size:120px;font-weight:500;color:#eef0f6;letter-spacing:2px;z-index:0}
.img{position:absolute}

/* hero */
.hero{left:0;top:0;width:1200px;height:640px;overflow:hidden}
.hero-bg{left:0;top:0;width:1200px;height:640px;background:linear-gradient(100deg,#0d1f6b 0%,#1b2e8a 35%,#3c4577 60%,#6f6e7a 80%,#2a2b36 100%)}
.nav{left:120px;top:20px;width:960px;height:50px;display:flex;align-items:center}
.nav ul{display:flex;gap:24px;list-style:none;margin-left:50px;font-size:12px;font-weight:500;color:#fff}
.nav ul li:first-child{color:#6f9bff}
.nav .phone{margin-left:auto;display:flex;align-items:center;gap:8px;color:#fff;font-size:16px;font-weight:500}
.icon-circle{width:24px;height:24px;border-radius:50%;border:2px solid #fff;display:flex;align-items:center;justify-content:center}
.hero h1{left:118px;top:160px;font-size:58px;line-height:61px;font-weight:700;color:#fff}
.hero h1 span{color:var(--blue)}
.hero p{left:120px;top:356px;width:380px;font-size:11.5px;line-height:18px;color:#fff}

/* about */
.about-ring{left:122px;top:668px;width:380px;height:380px;border-radius:50%;background:#e5eafc}
.about-photo{left:152px;top:700px;width:320px;height:320px;border-radius:50%;background:radial-gradient(circle at 45% 40%,#c49a86 0%,#8a6a5c 35%,#5a5e66 70%,#3b3f4b 100%)}
.about-wheel{left:355px;top:858px;width:150px;height:150px;border-radius:50%;background:radial-gradient(circle,#f5f5f5 0%,#a8a8ad 45%,#4a4a50 70%,#1a1a1e 100%)}
.about h2{left:592px;top:704px;font-size:38px;line-height:42px;font-weight:600;color:var(--ink)}
.about h2 span{color:var(--blue)}
.about .copy{left:593px;top:803px;width:470px;font-size:11.5px;line-height:19px;color:var(--muted)}
.about .copy p+p{margin-top:19px}
.about .copy b{color:var(--ink)}
.about .phone{left:792px;top:983px;display:flex;align-items:center;gap:8px;font-size:16px;font-weight:500;padding-left:14px;border-left:2px solid var(--line);height:34px}
.about .phone .icon-circle{border-color:var(--blue)}

/* features */
.feature{top:1094px;width:290px;height:156px;background:linear-gradient(#fff,#f4f6fc);border:1px solid #eceff8;border-radius:6px;z-index:1;text-align:center}
.feature .ico{width:56px;height:56px;border-radius:50%;background:var(--blue);border:4px solid #dfe6fd;margin:24px auto 10px;display:flex;align-items:center;justify-content:center}
.feature h3{font-size:15px;font-weight:600;color:var(--ink)}

/* services */
.services-band{left:0;top:1340px;width:1200px;height:660px}
.services h2{left:0;top:1400px;width:1200px;text-align:center;font-size:36px;font-weight:600;color:#fff}
.svc-list{left:122px;top:1480px;width:286px;list-style:none}
.svc-list li{height:60px;display:flex;align-items:center;padding-left:6px;border-bottom:1px solid rgba(255,255,255,.45);color:#fff;font-family:"Outfit",sans-serif;font-size:15px;font-weight:600}
.svc-list li.active{background:#fff;color:var(--blue);padding-left:18px;border-bottom-color:transparent}
.svc-stage{left:408px;top:1480px;width:670px;height:418px;background:#fff}
.svc-render{left:420px;top:1530px;width:370px;height:340px;border-radius:50%;background:radial-gradient(circle at 55% 50%,#8fb0ff 0%,#2b5af2 30%,#1a37c4 60%,#0c1b7a 85%,transparent 86%)}
.svc-panel{left:811px;top:1487px;width:259px;height:404px;background:var(--grey)}
.svc-panel .ico{position:absolute;left:36px;top:56px;width:48px;height:48px;border-radius:50%;border:2px solid #fff;display:flex;align-items:center;justify-content:center}
.svc-panel p{position:absolute;left:36px;top:126px;width:190px;font-size:11.5px;line-height:19px;color:#fff}

/* portfolio */
.section-title{position:absolute;left:0;width:1200px;text-align:center;font-family:"Outfit",sans-serif;font-size:36px;font-weight:600;color:var(--ink)}
.tile{position:absolute;border-radius:6px}

/* process */
.step{position:absolute;top:2766px;width:170px;height:170px}
.step .arc{position:absolute;left:0;top:14px;width:170px;height:156px}
.step .disc{position:absolute;left:14px;top:14px;width:142px;height:142px;border-radius:50%;background:var(--blue);display:flex;align-items:center;justify-content:center;text-align:center;color:#fff;font-family:"Outfit",sans-serif;font-size:16px;font-weight:600;line-height:18px;padding-top:22px}
.step .num{position:absolute;left:65px;top:0;width:40px;height:40px;border-radius:50%;background:#fff;border:2px solid var(--blue);display:flex;align-items:center;justify-content:center;font-family:"Outfit",sans-serif;font-weight:600;font-size:16px;color:var(--ink)}

/* blog */
.blog-bg{left:0;top:3042px;width:1200px;height:572px;background:var(--pale)}
.card{position:absolute;top:3152px;width:307px;height:328px;background:#fff;border-radius:4px;box-shadow:0 2px 8px rgba(30,40,90,.06)}
.card .thumb{position:absolute;left:18px;top:18px;width:288px;height:212px}
.card .date{position:absolute;left:18px;top:242px;font-size:10px;color:var(--blue);text-decoration:underline;font-weight:500}
.card h3{position:absolute;left:18px;top:260px;width:250px;font-size:14.5px;line-height:19px;font-weight:500;color:var(--ink)}
.card .go{position:absolute;right:8px;top:292px;width:20px;height:20px;border-radius:50%;background:var(--blue)}

/* contact */
.form-box{left:122px;top:3658px;width:466px;height:412px;background:#fff;box-shadow:0 2px 14px rgba(30,40,90,.08)}
.form-head{left:128px;top:3662px;width:456px;height:56px;background:var(--grey);color:#fff;font-family:"Outfit",sans-serif;font-size:34px;font-weight:600;display:flex;align-items:center;padding-left:38px}
.field{position:absolute;height:36px;border:1px solid #cfd3dd;font-size:11px;color:var(--muted);padding:10px 12px}
.map-ring{left:690px;top:3668px;width:340px;height:340px;border-radius:50%;background:#e6ebfb}
.map{left:710px;top:3688px;width:320px;height:320px;border-radius:50%;background:linear-gradient(135deg,#e9eef0 0%,#dfe8df 45%,#9fd0ec 65%,#6dbbe6 100%)}
.car{left:670px;top:3960px;width:340px;height:110px;border-radius:50% 50% 40% 40%/60% 60% 40% 40%;background:linear-gradient(#eef0f4,#b9bec8 60%,#6a6e77)}

/* cta + footer */
.footer-bg{left:0;top:4350px;width:1200px;height:386px;background:var(--dark)}
.cta{left:121px;top:4187px;width:958px;height:270px;border-radius:135px;background:linear-gradient(90deg,#2a52e0 0%,var(--blue) 45%);overflow:hidden}
.cta h2{position:absolute;left:423px;top:52px;font-size:37px;line-height:42px;font-weight:600;color:#fff}
.cta p{position:absolute;left:424px;top:140px;width:380px;font-size:11.5px;line-height:17px;color:#fff}
.foot{position:absolute;top:4500px;color:#fff}
.foot h4{font-family:"Outfit",sans-serif;font-size:15px;font-weight:600;margin-bottom:14px}
.foot ul{list-style:none;font-size:9px;line-height:21px;color:#c8c9d0}
.foot .row{display:flex;align-items:center;gap:10px;font-size:9px;color:#c8c9d0;margin-bottom:18px}
.foot .ring{width:24px;height:24px;border-radius:50%;border:1.5px solid #fff;flex:none}
.vline{position:absolute;top:4500px;width:1px;height:180px;background:#3a3a40}
.copyright{left:0;top:4713px;width:1200px;text-align:center;font-size:9px;color:#d4d4da}
</style>
</head>
<body>

<!-- HERO -->
<section class="hero abs">
  <div class="hero-bg abs img" role="img" aria-label="Engineer's hand at a laptop screen showing a blue wheel 3D model"></div>
  <svg class="abs" style="left:0;top:470px" width="1200" height="170" viewBox="0 0 1200 170">
    <path d="M0 40 Q600 250 1200 40 L1200 170 L0 170Z" fill="#fff"/>
    <path d="M0 40 Q520 230 1010 120 L1130 90 L1060 118 Q560 260 0 58Z" fill="var(--blue)"/>
    <path d="M1060 118 L1200 40 L1200 76 L1090 130Z" fill="#3b3b40"/>
  </svg>
  <nav class="nav abs">
    <div class="logo"><span class="mark"></span>valtro</div>
    <ul><li>Home</li><li>About Us</li><li>Our Services</li><li>Portfolio</li><li>Case Studies</li></ul>
    <div class="phone"><span class="icon-circle"><svg width="12" height="12" viewBox="0 0 24 24"><path d="M6 2l4 5-2 3a12 12 0 006 6l3-2 5 4-3 4C10 22 2 14 2 5z" fill="#fff"/></svg></span>+44 (0) 7700 900418</div>
    <div class="btn" style="position:relative;margin-left:28px;height:30px;padding-left:14px;font-size:11px;gap:10px">Contact Us<span class="dot" style="width:22px;height:22px"><i style="width:11px;height:11px"></i></span></div>
  </nav>
  <h1 class="abs">Precision<br>Mechanical &amp;<br>Product <span>Design</span></h1>
  <p class="abs">UK-based mechanical and product design consultancy delivering complete solutions from concept to full-scale production.</p>
  <div class="btn" style="left:120px;top:418px;width:142px">Get Started<span class="dot"><i></i></span></div>
</section>

<!-- ABOUT -->
<section class="about">
  <div class="about-ring abs"></div>
  <svg class="abs" style="left:440px;top:780px" width="70" height="200" viewBox="0 0 70 200"><path d="M10 0 A170 170 0 0 1 40 190" stroke="#e3e8fb" stroke-width="14" fill="none"/></svg>
  <div class="about-photo abs img" role="img" aria-label="Portrait of the chief engineer"></div>
  <div class="about-wheel abs img" role="img" aria-label="Polished alloy wheel"></div>
  <h2 class="abs">About Valtro<br>Mechanical <span>Design.</span></h2>
  <div class="copy abs">
    <p>Welcome to Valtro Mechanical Design. We are a UK based design consultancy offering a comprehensive mechanical and product design service from initial concepts through to full volume production.</p>
    <p>Rhys Callow is the Chief Engineer at Valtro Mechanical Design. He has <b>11 years experience</b> working as a mechanical design engineer in multiple industries including <b>high performance automotive, consumer products, medical, industrial plus</b> many more. He has worked in multiple roles across a wide range of products.</p>
  </div>
  <div class="btn" style="left:590px;top:980px;width:178px">Read More About Us<span class="dot"><i></i></span></div>
  <div class="phone abs"><span class="icon-circle"><svg width="12" height="12" viewBox="0 0 24 24"><path d="M6 2l4 5-2 3a12 12 0 006 6l3-2 5 4-3 4C10 22 2 14 2 5z" fill="var(--blue)"/></svg></span>+44 (0) 7700 900418</div>
</section>

<div class="watermark" style="top:1180px">Valtro Mechanical Design</div>
<div class="feature abs" style="left:130px"><div class="ico"><svg width="24" height="24" viewBox="0 0 24 24" fill="none" stroke="#fff" stroke-width="2"><path d="M12 2l9 5v10l-9 5-9-5V7z"/><path d="M12 12l9-5M12 12v10M12 12L3 7"/></svg></div><h3>Bespoke Product Design</h3></div>
<div class="feature abs" style="left:455px"><div class="ico"><svg width="24" height="24" viewBox="0 0 24 24" fill="none" stroke="#fff" stroke-width="2"><path d="M12 2l5 3v6l-5 3-5-3V5z"/><path d="M7 11l5 3v7l-5 2-5-3v-6zM17 11l5 3v6l-5 3-5-2v-7z"/></svg></div><h3>3D Modelling and Drawings</h3></div>
<div class="feature abs" style="left:780px"><div class="ico"><svg width="24" height="24" viewBox="0 0 24 24" fill="none" stroke="#fff" stroke-width="2"><rect x="3" y="14" width="18" height="7"/><path d="M8 14V8h8v6M12 8V3"/></svg></div><h3>Design for Manufacture</h3></div>

<!-- SERVICES -->
<section class="services">
  <svg class="services-band abs" viewBox="0 0 1200 660">
    <path d="M0 120 Q600 -40 1200 120 L1200 540 Q600 700 0 540Z" fill="var(--blue)"/>
    <path d="M0 100 L100 70 L110 92 L0 130Z" fill="#3b3b40"/>
    <path d="M1100 560 L1200 530 L1200 566 L1110 590Z" fill="#3b3b40"/>
    <path d="M0 100 Q600 -70 1200 100" stroke="var(--blue)" stroke-width="6" fill="none"/>
    <path d="M0 560 Q600 720 1200 560" stroke="var(--blue)" stroke-width="6" fill="none"/>
  </svg>
  <h2 class="abs">Our Services</h2>
  <ul class="svc-list abs">
    <li>01.&nbsp; Mechanical Design</li>
    <li>02.&nbsp; Design Consultancy</li>
    <li class="active"><svg width="22" height="14" viewBox="0 0 22 14" style="margin-right:8px"><path d="M1 1l6 6-6 6M9 1l6 6-6 6" stroke="var(--blue)" stroke-width="3" fill="none"/></svg>03.&nbsp; 3D Printing</li>
    <li>04.&nbsp; Project Management</li>
    <li>05.&nbsp; Design for Manufacture</li>
    <li>06.&nbsp; TIG Welding</li>
    <li>07.&nbsp; Painting</li>
  </ul>
  <div class="svc-stage abs"></div>
  <div class="svc-render abs img" role="img" aria-label="Blue 3D render of a spoked wheel with stress analysis labels"></div>
  <div class="svc-panel abs">
    <div class="ico"><svg width="22" height="22" viewBox="0 0 24 24" fill="none" stroke="#fff" stroke-width="2"><path d="M12 2l5 3v6l-5 3-5-3V5z"/><path d="M7 11l5 3v7l-5 2-5-3v-6zM17 11l5 3v6l-5 3-5-2v-7z"/></svg></div>
    <p>We can manufacture low volume functional prototypes using 3D printing. Prototype manufacture is an essential part of the design process to prove out it's functionality, aesthetics and durability. We can provide you with a fully finished product ready for testing.</p>
  </div>
  <div class="btn" style="left:847px;top:1806px;width:148px">View services<span class="dot"><i></i></span></div>
</section>

<!-- PORTFOLIO -->
<h2 class="section-title" style="top:2052px">Our Portfolio</h2>
<div class="tile img" role="img" aria-label="Planetary gearbox with steel gears" style="left:116px;top:2124px;width:312px;height:225px;background:radial-gradient(circle,#c9ccd2,#6a6f78 60%,#3d4048)"></div>
<div class="tile img" role="img" aria-label="Wooden pen resting in a turned wooden stand" style="left:435px;top:2124px;width:319px;height:456px;background:linear-gradient(160deg,#1b1b1d,#3a3a3c 45%,#8a5a32 70%,#2a2a2c)"></div>
<div class="tile img" role="img" aria-label="Dark engine assembly on a green-lit background" style="left:761px;top:2124px;width:311px;height:225px;background:radial-gradient(circle at 55% 55%,#6a6d70,#1d2620 55%,#0b130d)"></div>
<div class="tile img" role="img" aria-label="Black machine housing with a handle and red feet" style="left:116px;top:2358px;width:312px;height:225px;background:linear-gradient(150deg,#ececee,#c9c9cc 45%,#2b2b2e 75%)"></div>
<div class="tile img" role="img" aria-label="Action camera on a brass telescopic mount" style="left:761px;top:2358px;width:311px;height:225px;background:linear-gradient(160deg,#f2f2f2,#dadada 50%,#b8a14a 70%,#2d2d2d)"></div>
<div class="btn" style="left:505px;top:2613px;width:180px">View All Protfolio<span class="dot"><i></i></span></div>

<!-- PROCESS -->
<h2 class="section-title" style="top:2680px">Our Process</h2>
<div class="step" style="left:121px"><svg class="arc" viewBox="0 0 170 156"><path d="M4 70 A81 81 0 0 0 166 70" stroke="var(--blue)" stroke-width="1.5" fill="none"/></svg><div class="disc">Discovery</div><div class="num">01</div></div>
<div class="step" style="left:316px"><svg class="arc" viewBox="0 0 170 156"><path d="M4 70 A81 81 0 0 0 166 70" stroke="var(--blue)" stroke-width="1.5" fill="none"/></svg><div class="disc">Concept</div><div class="num">02</div></div>
<div class="step" style="left:516px"><svg class="arc" viewBox="0 0 170 156"><path d="M4 70 A81 81 0 0 0 166 70" stroke="var(--blue)" stroke-width="1.5" fill="none"/></svg><div class="disc">Detailed<br>Design</div><div class="num">03</div></div>
<div class="step" style="left:720px"><svg class="arc" viewBox="0 0 170 156"><path d="M4 70 A81 81 0 0 0 166 70" stroke="var(--blue)" stroke-width="1.5" fill="none"/></svg><div class="disc">Prototype</div><div class="num">04</div></div>
<div class="step" style="left:908px"><svg class="arc" viewBox="0 0 170 156"><path d="M4 70 A81 81 0 0 0 166 70" stroke="var(--blue)" stroke-width="1.5" fill="none"/></svg><div class="disc">Production<br>Launch</div><div class="num">05</div></div>
<div class="watermark" style="top:2930px;left:40px">Valtro Mechanical Design</div>

<!-- BLOG -->
<div class="blog-bg abs"></div>
<h2 class="section-title" style="top:3086px">Latest Blog</h2>
<article class="card" style="left:121px"><div class="thumb img" role="img" aria-label="Engineer working on CAD models across two monitors" style="background:linear-gradient(160deg,#3c4754,#1f262e 55%,#5a4a3e)"></div><span class="date">November 15, 2022, Read</span><h3>Designing for Manufacture: How to Reduce Cost &amp; Lead Time</h3><span class="go"></span></article>
<article class="card" style="left:446px"><div class="thumb img" role="img" aria-label="Hand sketching a technical drawing with a pen" style="background:linear-gradient(160deg,#f1f1f1,#d9d9d9 60%,#9a9a9a)"></div><span class="date">November 15, 2022, Read</span><h3>The Role of Tolerance Analysis in High-Precision Engineering</h3><span class="go"></span></article>
<article class="card" style="left:771px"><div class="thumb img" role="img" aria-label="3D printer head under purple and green light" style="background:linear-gradient(160deg,#5a2a7a,#2a2436 50%,#2d9b4a)"></div><span class="date">November 15, 2022, Read</span><h3>How to Prepare a Supplier Ready Engineering Package</h3><span class="go"></span></article>
<div class="btn" style="left:528px;top:3512px;width:144px">View All Blog<span class="dot"><i></i></span></div>

<!-- CONTACT -->
<div class="form-box abs"></div>
<div class="form-head abs">Let's Work Together.</div>
<div class="field" style="left:133px;top:3746px;width:219px">Frist Name*</div>
<div class="field" style="left:358px;top:3746px;width:219px">Last Name*</div>
<div class="field" style="left:133px;top:3788px;width:219px">Email*</div>
<div class="field" style="left:358px;top:3788px;width:219px">Phone*</div>
<div class="field" style="left:133px;top:3830px;width:444px;height:100px">Mesage*</div>
<div class="btn" style="left:267px;top:3963px;width:178px">Submit<span class="dot"><i></i></span></div>
<div class="map-ring abs"></div>
<div class="map abs img" role="img" aria-label="Road map of South Wales with a location pin"></div>
<div class="car abs img" role="img" aria-label="Silver classic saloon car"></div>
<div class="watermark" style="top:4065px">Valtro Mechanical Design</div>

<!-- CTA + FOOTER -->
<div class="footer-bg abs"></div>
<svg class="abs" style="left:0;top:4300px" width="1200" height="120" viewBox="0 0 1200 120"><path d="M0 120 L0 96 L100 60 L110 80 L60 120Z" fill="#3b3b40"/><path d="M1080 70 L1200 110 L1200 120 L1080 90Z" fill="#3b3b40"/></svg>
<section class="cta abs">
  <h2>Start Your Project with<br>a Technical Review</h2>
  <p>Tell us about your product or challenge, and we'll provide a clear next-step recommendation.</p>
  <div class="btn light" style="left:425px;top:188px;width:138px">Get Started<span class="dot"><i></i></span></div>
</section>

<div class="foot" style="left:122px"><div class="logo" style="font-size:26px;margin-bottom:18px"><span class="mark"></span>valtro</div><p style="width:180px;font-size:9px;line-height:15px;color:#c8c9d0">We are a UK based design consultancy offering a comprehensive mechanical and product design service from initial concepts through to full volume production.</p></div>
<span class="vline" style="left:322px"></span>
<div class="foot" style="left:376px"><h4>Main Links</h4><ul><li>Home</li><li>About Us</li><li>Services</li><li>Portfolio</li><li>Case studies</li></ul></div>
<span class="vline" style="left:512px"></span>
<div class="foot" style="left:560px"><h4>Contact Us</h4>
  <div class="row"><span class="ring"></span>South Wales, UK</div>
  <div class="row"><span class="ring"></span>+44 (0) 7700 900418</div>
  <div class="row"><span class="ring"></span><span style="color:#7b9bff">info@valtrobuild.design</span></div>
</div>
<span class="vline" style="left:725px"></span>
<div class="foot" style="left:775px"><h4>Services</h4><ul><li>Mechanical Design</li><li>Design Consultancy</li><li>3D Printing</li><li>Project Management</li><li>Design for Manufacture (DFM)</li><li>TIG Welding</li><li>Painting</li></ul></div>
<span class="vline" style="left:910px"></span>
<div class="foot" style="left:960px"><h4>Popular Brands</h4>
  <div class="row"><span class="ring"></span>Pagebook</div>
  <div class="row"><span class="ring"></span>Viewtube</div>
  <div class="row"><span class="ring"></span>Linkwork</div>
</div>
<div class="copyright abs">Copyright © 2025 Valtro Mechanical Design All Rights Reserved</div>

</body>
</html>
```